Harborline Stay Collective Business Card Design

Design a business card for Harborline Stay Collective. Look at the website for colors and reference. Card should have logo, name, title, office number, mobile number, email, URL and a tagline like, "Luxury Hotel & Resort Email Marketing" (This might change).

https://www.harborlinestaycollective.net

The rest I will leave up to your imagination.

Contact Information for Business Card

Logo, name, title, office number, mobile number, email, URL and a tagline like, "Luxury Hotel & Resort Email Marketing" (This might change).

```html
<!DOCTYPE html>
<html lang="en">
<head>
<meta charset="utf-8">
<title>Harborline Stay Collective – Business Card</title>
<link href="https://fonts.googleapis.com/css2?family=Open+Sans:wght@400;600;700;800&display=swap" rel="stylesheet">
<style>
  :root {
    --backdrop: #3b3b3b;
    --card: #1b1b1b;
    --orange: #f47a20;
    --white: #f2f2f2;
    --silver: #b9b9b9;
    --muted: #d6d6d6;
  }
  * { box-sizing: border-box; margin: 0; padding: 0; }
  html, body {
    width: 1200px; height: 801px; overflow: hidden;
    background: var(--backdrop);
    font-family: "Open Sans", Arial, sans-serif;
  }
  .stage {
    width: 1200px; height: 801px;
    display: flex; align-items: center; justify-content: center; gap: 50px;
  }
  .card {
    width: 525px; height: 300px;
    background: var(--card);
    border: 2px solid var(--orange);
    position: relative;
  }
  /* Front */
  .card--front { padding: 34px 36px 28px; }
  .brand-name {
    display: flex; align-items: center; gap: 12px;
    color: var(--white); font-weight: 800; font-size: 27px;
    text-transform: uppercase; letter-spacing: 0.5px; line-height: 1;
  }
  .brand-name .brand-dot {
    width: 14px; height: 14px; background: var(--orange); flex: none;
  }
  .details {
    display: flex; align-items: center; margin-top: 58px;
  }
  .person { width: 190px; }
  .person-name {
    color: var(--orange); font-weight: 700; font-size: 20px;
    text-transform: uppercase; line-height: 1.1;
  }
  .person-title { color: var(--white); font-size: 15px; margin-top: 4px; }
  .divider {
    width: 1px; height: 58px; background: var(--orange); margin: 0 22px;
  }
  .contacts { list-style: none; }
  .contacts li {
    display: flex; align-items: center; gap: 8px;
    color: var(--muted); font-size: 13px; line-height: 1.55;
  }
  .contacts svg { width: 11px; height: 11px; flex: none; }
  .tagline {
    position: absolute; left: 36px; bottom: 28px;
    color: var(--white); font-size: 15px;
  }
  /* Back */
  .card--back { display: flex; align-items: center; justify-content: center; }
  .back-name {
    color: var(--silver); font-weight: 800; font-size: 30px;
    text-transform: uppercase; letter-spacing: 0.5px; text-align: center; line-height: 1.15;
  }
</style>
</head>
<body>
<main class="stage">
  <section class="card card--front" aria-label="Business card front">
    <div class="brand-name"><span class="brand-dot"></span>Harborline Stay Collective</div>
    <div class="details">
      <div class="person">
        <p class="person-name">Dorian Vale</p>
        <p class="person-title">President / CEO</p>
      </div>
      <div class="divider"></div>
      <ul class="contacts">
        <li>
          <svg viewBox="0 0 12 12" aria-hidden="true"><path fill="#f47a20" d="M2.4 0.8l1.8 0 0.8 2.6-1.2 1c0.6 1.4 1.6 2.4 3 3l1-1.2 2.6 0.8 0 1.8c0 0.6-0.5 1.2-1.2 1.2C4.6 10 0.8 6.2 0.8 2C0.8 1.3 1.4 0.8 2.4 0.8z"/></svg>
          555.214.3080
        </li>
        <li>
          <svg viewBox="0 0 12 12" aria-hidden="true"><rect x="0.5" y="2" width="11" height="8" fill="#f47a20"/><path d="M0.8 2.4L6 6.6 11.2 2.4" fill="none" stroke="#1b1b1b" stroke-width="1"/></svg>
          info@harborlinestaycollective.net
        </li>
        <li>
          <svg viewBox="0 0 12 12" aria-hidden="true"><circle cx="6" cy="6" r="5.5" fill="#f47a20"/><path d="M0.8 6h10.4M6 0.5c-2.2 2.8-2.2 8.2 0 11M6 0.5c2.2 2.8 2.2 8.2 0 11" fill="none" stroke="#1b1b1b" stroke-width="0.8"/></svg>
          www.harborlinestaycollective.net
        </li>
      </ul>
    </div>
    <p class="tagline">Luxury Hotel &amp; Resort Email Marketing</p>
  </section>

  <section class="card card--back" aria-label="Business card back">
    <p class="back-name">Harborline<br>Stay Collective</p>
  </section>
</main>
</body>
</html>
```